Redesign company trifold brochure

We are rebranding our company in September and looking for a more professional design for our brochure.

What we do - providing interdisciplinary care for those supporting ill, elderly and special needs pets at home following the human hospice model of care - is very novel and our brochure is key in explaining it and our offerings.

We serve dogs and cats. Most of the animals are quite sick, elderly. I have many personal and stock photos we can use in the brochure. Please - no pictures of puppies and/or kittens.

The hard part is fitting the info and message into a clear and concise format.

It must be appealing both to pet owners and vets (who are our primary source of patients through referrals).

It should covey WARMTH, COMPASSION, PROFESSIONALISM, and EXPERTISE.

Please look at our website www.LarkvaleAnimalRest.com for more info

We have until now used maroon and copper for colors - to reflect the "sunset" of the pets life. BUT are now changing to Navy, Teal and White to reflect calm, trust and competence.

We will use the same logo recolored.

Existing brochure and new logo are attached.

PLEASE ask questions!!
Updates

We have a library of stock images you are welcome to use. All have been legally acquired and we have the right to use them. You DO NOT have to use them, just sending along in case you wish to. https://www.filecrate.example/sh/q7rmt2wzp40kdyh/BBR8Kxtz-Pqmn3vd7yHsLcWqe?dl=0

Our colors are NAVY, TEAL and WHITE. For your reference, the navy we use is 99/87/44/55 (CMYK) The Teal we use is 76/11/44/0 (CMYK) Thank you!

Designers -- pleaseuse pictures of older pets (no puppies or kittens). Below is a link to stock photos we own that would be appropriate for use in the brochure. https://www.filecrate.example/sh/k416f8m2twr5zqa/BBQe3LmxtvRVZWPgb8JTFYs_4m?dl=0 THANK YOU!

Designers -- I would VERY much like to include a photo of a pet in a wheel chair. I have personal photos as well as (purchased) stock photos for this purpose which can be found at http://lnkr.example/LARWC-Pets-in-Wheelchairs Thank you!!

Today is the last day! Many of you have submitted beautiful designs and others are rolling in. I am so appreciative of your time and energy!! Please do not let the deadline pass without YOUR very BEST entry being submitted!! Thank you! - Miriam & All of us at Larkvale Animal Rest & Comfort Care

Target Market(s)

Pet Owners and Veterinarians

Industry/Entity Type

Pet Care

Font styles to use
Serif

Colors
0455a3
33b8a4
ffffff

Requirements
Must have
• Our logo and information about our services. Pictures of pets. Our contact info. PLEASE NOTE: this is a 2 sided brochure. Please submit both inside and outside.
Should not have
• puppies, kittens - anything off message

```html
<!DOCTYPE html>
<html lang="en">
<head>
<meta charset="utf-8">
<title>Larkvale Animal Rest &amp; Comfort Care – Trifold Brochure</title>
<link rel="stylesheet" href="https://fonts.googleapis.com/css2?family=Federo&family=Questrial&family=Arimo&family=Lora:ital@1&display=swap">
<style>
  :root {
    --navy: #0e1f42;
    --teal: #25a89c;
    --white: #ffffff;
    --ink: #18243f;
    --rule: #333333;
    --backdrop: #ebe7e1;
  }
  * { box-sizing: border-box; margin: 0; padding: 0; }
  html, body { width: 1200px; height: 943px; overflow: hidden; background: var(--backdrop); }
  .canvas { position: relative; width: 1200px; height: 943px; }
  .shapes { position: absolute; inset: 0; }

  .believe-title {
    position: absolute; left: 47px; top: 410px;
    font: 400 32px/1 "Federo", sans-serif; letter-spacing: 0.5px; color: var(--navy);
  }
  .believe-list {
    position: absolute; left: 48px; top: 453px; width: 350px;
    list-style: none; white-space: nowrap;
    font: 15.4px/21.5px "Questrial", sans-serif; color: var(--ink);
  }
  .believe-list li { position: relative; padding-left: 21px; margin-bottom: 16.5px; }
  .believe-list li::before { content: "➢"; position: absolute; left: 2px; top: 0; font-size: 12px; }

  .brand {
    position: absolute; text-align: center;
    font-family: "Federo", sans-serif; color: var(--navy);
  }
  .brand-mark { display: block; margin: 0 auto 8px; border-radius: 50%; background: var(--teal); }
  .brand-center { left: 440px; top: 590px; width: 320px; font-size: 25px; line-height: 28px; }
  .brand-center .brand-mark { width: 46px; height: 46px; }
  .brand-top { left: 815px; top: 50px; width: 320px; font-size: 23px; line-height: 26px; }
  .brand-top .brand-mark { width: 42px; height: 42px; }

  .contact {
    position: absolute; left: 423px; top: 723px; width: 353px;
    text-align: center; font: 13.5px/1 "Arimo", sans-serif; color: var(--ink);
  }
  .contact p { margin-bottom: 12.5px; }
  .contact .address { line-height: 18px; }
  .contact-rule { position: absolute; left: 423px; top: 842px; width: 353px; height: 1.5px; background: var(--rule); }
  .social {
    position: absolute; left: 505px; top: 850px;
    font: 15px/24px "Arimo", sans-serif; color: var(--ink);
  }
  .social p { display: flex; align-items: center; gap: 6px; }
  .social .dot { width: 15px; height: 15px; border-radius: 2px; background: var(--navy); }

  .cover-heading {
    position: absolute; left: 787px; top: 788px; width: 378px;
    text-align: center; font: 400 24px/28px "Federo", sans-serif; letter-spacing: 0.6px;
    white-space: nowrap; color: var(--white);
  }
  .cover-tagline {
    position: absolute; left: 787px; top: 867px; width: 378px;
    text-align: center; font: italic 18.5px/1 "Lora", serif; color: var(--white);
  }
</style>
</head>
<body>
<main class="canvas">
  <svg class="shapes" viewBox="0 0 1200 943" width="1200" height="943">
    <defs>
      <linearGradient id="tone-companions" x1="0" y1="0" x2="1" y2="1">
        <stop offset="0" stop-color="#f3efe9"/>
        <stop offset="0.45" stop-color="#b5763f"/>
        <stop offset="1" stop-color="#c9c4c4"/>
      </linearGradient>
      <linearGradient id="tone-meadow" x1="0" y1="0" x2="0.4" y2="1">
        <stop offset="0" stop-color="#cfdcb0"/>
        <stop offset="0.5" stop-color="#e9e2bf"/>
        <stop offset="1" stop-color="#a9c85a"/>
      </linearGradient>
      <linearGradient id="tone-resting" x1="0" y1="0" x2="0.6" y2="1">
        <stop offset="0" stop-color="#e8b9b3"/>
        <stop offset="0.45" stop-color="#e3cfae"/>
        <stop offset="1" stop-color="#dc8a9a"/>
      </linearGradient>
      <clipPath id="inside-photos">
        <path d="M35,35 H787 V322 C600,395 300,410 35,345 Z"/>
      </clipPath>
      <filter id="sheet-shadow" x="-5%" y="-5%" width="110%" height="110%">
        <feDropShadow dx="0" dy="3" stdDeviation="4" flood-opacity="0.3"/>
      </filter>
    </defs>

    <rect x="35" y="35" width="1130" height="870" fill="var(--white)" filter="url(#sheet-shadow)"/>

    <rect x="35" y="340" width="373" height="565" fill="var(--teal)"/>

    <g clip-path="url(#inside-photos)">
      <rect role="img" aria-label="Photo: an older dog resting beside a grey cat" x="35" y="35" width="373" height="390" fill="url(#tone-companions)"/>
      <rect role="img" aria-label="Photo: a pale older dog sitting in a sunlit meadow with its owner" x="408" y="35" width="379" height="390" fill="url(#tone-meadow)"/>
    </g>

    <path d="M35,345 C300,410 600,395 787,322 L787,345 C600,412 300,418 35,360 Z" fill="var(--teal)"/>
    <path d="M35,352 C300,416 600,405 787,336 L787,350 C600,440 360,455 35,362 Z" fill="var(--navy)"/>

    <path d="M787,200 Q980,170 1165,212 L1165,228 Q980,188 787,230 Z" fill="var(--teal)"/>
    <path d="M787,222 Q980,186 1165,226 L1165,905 L787,905 Z" fill="var(--navy)"/>
    <path role="img" aria-label="Photo: an elderly golden dog resting its head on a soft toy" d="M787,240 Q980,218 1165,242 L1165,702 Q1000,742 787,722 Z" fill="url(#tone-resting)"/>
    <path d="M880,742 Q1050,740 1165,700 L1165,714 Q1050,752 880,744 Z" fill="var(--teal)"/>
  </svg>

  <h2 class="believe-title">We Believe</h2>
  <ul class="believe-list">
    <li>That animals are conscious beings, capable of<br>thought, feeling, emotion and choice.</li>
    <li>That each animal is an individual with his or<br>her unique needs and whishes.</li>
    <li>That all pets deserve to be pain-free.</li>
    <li>That the principles of human hospice and<br>palliative care are equally powerful when<br>applied to animals</li>
    <li>That an interdisciplinary team is essential to<br>addressing that needs of pets and their<br>families through aging and illness.</li>
    <li>That quality of life is subjective best evaluated<br>by the family who knows and loves the<br>animal.</li>
    <li>That there isn't are answer that is right for<br>every animal or every family</li>
  </ul>

  <div class="brand brand-center">
    <span class="brand-mark"></span>
    Larkvale Animal Rest<br>&amp; Comfort Care
  </div>
  <div class="contact">
    <p>Contact us (508) 441-LARK</p>
    <p>info@LarkvaleAnimalRest.com</p>
    <p>www.LarkvaleAnimalRest.com</p>
    <p class="address">212 Meadowfield Lane,<br>Suite 40 Larkvale, Ma 01920</p>
  </div>
  <div class="contact-rule"></div>
  <div class="social">
    <p><span class="dot"></span>LarkvaleAnimalRest</p>
    <p><span class="dot"></span>LarkvaleRest</p>
  </div>

  <div class="brand brand-top">
    <span class="brand-mark"></span>
    Larkvale Animal Rest<br>&amp; Comfort Care
  </div>
  <h1 class="cover-heading">Skilled Home Care for Ill, Elderly<br>and Special Needs Animals</h1>
  <p class="cover-tagline">Compassionate Support for Families</p>
</main>
</body>
</html>
```